Business Card Re-design

We are looking for a fresh bold look for general office business cards. We are a staffing agency that staffs industrial, coal mining, and clerical jobs.
Tag Line: We pair the RIGHT talent with the RIGHT work.
Marlow Falls Office: 2473 W. Tallow Creek Rd, Marlow Falls, OH - 47308
p. 555.203.6180 f. 555.203.6195
Ashford Office: 264 S. Birch Ln, Ashford, OH - 47152
p. 555.319.2047 f. 555.203.6195
Absentee/Emergency 24hr Hotline 555.203.6172 opt.1
www.bluelanternworkforce.example

```html
<!DOCTYPE html>
<html lang="en">
<head>
<meta charset="utf-8">
<title>Blue Lantern Workforce – Business Card</title>
<link rel="stylesheet" href="https://fonts.googleapis.com/css2?family=Bebas+Neue&display=swap">
<style>
  :root {
    --backdrop: #1a5bb5;
    --navy: #0b2f7e;
    --ink-navy: #123a8a;
    --green: #3cc61a;
    --white: #ffffff;
    --paper: #f7f7f5;
  }
  * { box-sizing: border-box; margin: 0; padding: 0; }
  html, body { width: 1200px; height: 800px; overflow: hidden; }
  body {
    background: var(--backdrop);
    font-family: "Bebas Neue", "Arial Narrow", sans-serif;
    display: flex;
    align-items: center;
    justify-content: center;
    gap: 60px;
  }
  .card {
    width: 525px;
    height: 300px;
    border-radius: 4px;
    position: relative;
    box-shadow: 0 10px 28px rgba(0, 0, 0, 0.25);
    overflow: hidden;
  }

  /* Front face */
  .card-front {
    background: var(--navy);
    color: var(--white);
    display: flex;
    flex-direction: column;
    align-items: center;
    justify-content: center;
  }
  .brand-name {
    font-size: 50px;
    font-weight: 400;
    line-height: 0.95;
    letter-spacing: 1px;
    text-align: center;
    color: var(--white);
    margin-bottom: 30px;
  }
  .tagline {
    position: absolute;
    bottom: 28px;
    left: 0;
    right: 0;
    text-align: center;
    font-size: 19px;
    letter-spacing: 1.2px;
  }
  .tagline .accent { color: var(--green); }
  .tagline .strong { color: var(--white); }

  /* Back face */
  .card-back {
    background: var(--paper);
    color: var(--ink-navy);
    padding: 24px 30px;
  }
  .office { margin-bottom: 10px; }
  .office-title {
    color: var(--green);
    font-size: 24px;
    font-weight: 400;
    line-height: 1;
    margin-bottom: 3px;
  }
  .contact-row {
    display: flex;
    font-size: 18px;
    line-height: 1.1;
  }
  .contact-row .label {
    color: var(--green);
    width: 20px;
    flex: none;
  }
  .hotline-title {
    font-size: 18px;
    line-height: 1.1;
  }
</style>
</head>
<body>

  <section class="card card-back" aria-label="Card back with office contacts">
    <div class="office">
      <h2 class="office-title">Marlow Falls Office</h2>
      <p class="contact-row"><span class="label">A</span>2473 W. Tallow Creek Rd, Marlow Falls, OH - 47308</p>
      <p class="contact-row"><span class="label">P</span>555.203.6180</p>
      <p class="contact-row"><span class="label">F</span>555.203.6195</p>
    </div>
    <div class="office">
      <h2 class="office-title">Ashford Office</h2>
      <p class="contact-row"><span class="label">A</span>264 S. Birch Ln, Ashford, OH - 47152</p>
      <p class="contact-row"><span class="label">P</span>555.319.2047</p>
      <p class="contact-row"><span class="label">F</span>555.203.6195</p>
    </div>
    <div class="hotline">
      <p class="hotline-title">Absentee/Emergency 24hr Hotline</p>
      <p class="contact-row"><span class="label">P</span>555.203.6172 opt.1</p>
      <p class="contact-row"><span class="label">W</span>www.bluelanternworkforce.example</p>
    </div>
  </section>

  <section class="card card-front" aria-label="Card front">
    <h1 class="brand-name">Blue Lantern<br>Workforce</h1>
    <p class="tagline">
      <span class="accent">We pair the</span>
      <span class="strong">Right talent</span>
      <span class="accent">with the</span>
      <span class="strong">Right work</span>
    </p>
  </section>

</body>
</html>
```